Business Card Design for Pastor/Church Leadership - simple, elegant, "different"

Design a name card based on logo and color from our branding guide - see file "MBF Logo and Color".
The teal frame around the logo is not part of the logo and is a not necessary design element for the name card (as the attached PDF file may suggest).
The font suggested by branding is "Frutiger 55 Roman".
The file "not good.pdf", a sample of a name card that is NOT good.
- fonts too small to read
- the tagline on the logo "Still waters, open door" not easy to read with logo used in this design
- "MAPLE GROVE FELLOWSHIP" unnecessarily duplicated - possibly because logo too small
- not sure about the green frame, probably better to drop

Target Market(s)

broad, all people the pastor of an international church in Tokyo meets

Industry/Entity Type

Business

Contact Information for Business Card

Mattias R. Pellworth
Pastor
3-9-4 Kawaranodai, Minori-ku
Tokyo 190-0412 (Church)
2-21 Ochibamachi, Minori-ku
Tokyo 190-0427 (Home)
Tel: 03-5817-2963
E-mail: pastor@maplegrovefell.org
URL: http://www.maplegrovefell.org

Font styles to use
Sans Serif
Other font styles liked:
• Frutiger 55 Roman (want, not must)

Requirements
Must have
• must include logo
• must make use of the "bright turquoise color"
• Cyan = 59, Magenta = 0, Yellow=24, Black=0
• Red=3.1%, Green=91%, Blue=87.1%
• Key Info (name) must be easy to read (see notes on bad sample namecard attached)

```html
<!DOCTYPE html>
<html lang="en">
<head>
<meta charset="utf-8">
<title>Maple Grove Fellowship – Pastor Name Card</title>
<link href="https://fonts.googleapis.com/css2?family=Source+Sans+3:wght@400;700&display=swap" rel="stylesheet">
<style>
  :root {
    --teal: #5bc5c8;
    --white: #ffffff;
    --fold-shadow: #e4e4e4;
    --backdrop: #3d3d3d;
  }
  * { margin: 0; padding: 0; box-sizing: border-box; }
  html, body {
    width: 1200px; height: 1200px; overflow: hidden;
    background: var(--backdrop);
    font-family: "Source Sans 3", sans-serif;
  }
  .card {
    position: absolute;
    left: 251px;
    width: 698px; height: 394px;
    overflow: hidden;
  }
  .card--front { top: 180px; background: var(--white); }
  .card--back  { top: 625px; background: var(--teal); color: var(--white); }
  .card__swoosh { position: absolute; inset: 0; width: 100%; height: 100%; }
  .line {
    position: absolute;
    transform: translate(-50%, -50%);
    white-space: nowrap;
    text-align: center;
    line-height: 1;
  }
  .brand-mark { font-weight: 700; font-size: 58px; letter-spacing: 2px; }
  .brand-name { font-weight: 700; font-size: 19px; letter-spacing: 0.2px; }
  .brand-rule { position: absolute; height: 2px; transform: translateX(-50%); }
  .brand-tagline { font-size: 18px; }

  .card--front .brand { color: var(--teal); }
  .card--front .brand-rule { background: var(--teal); }
  .card--back .brand-rule { background: var(--white); }

  .contact { color: var(--white); }
  .contact__name { font-weight: 700; font-size: 26px; }
  .contact__role { font-size: 18px; }
  .contact__phone { font-size: 19px; }
  .contact__detail { font-size: 17px; }
  .card__url { font-size: 18px; }
</style>
</head>
<body>

<section class="card card--front">
  <svg class="card__swoosh" viewBox="0 0 872 493" preserveAspectRatio="none" aria-hidden="true">
    <path fill="var(--fold-shadow)" d="M358,20 C330,90 330,190 385,290 C430,370 480,435 530,493 L566,493 Z"/>
    <path fill="var(--teal)" d="M371,0 C338,70 336,190 400,295 C452,380 510,440 566,493 L872,493 L872,0 Z"/>
  </svg>

  <div class="brand">
    <div class="line brand-mark" style="left:158px; top:158px;">MBF</div>
    <div class="line brand-name" style="left:158px; top:248px;">MAPLE GROVE FELLOWSHIP</div>
    <div class="brand-rule" style="left:158px; top:265px; width:232px;"></div>
    <div class="line brand-tagline" style="left:158px; top:284px;">Still waters, open door</div>
  </div>

  <div class="contact">
    <div class="line contact__name" style="left:533px; top:73px;">Mattias R. Pellworth</div>
    <div class="line contact__role" style="left:533px; top:99px;">Pastor</div>
    <div class="line contact__phone" style="left:533px; top:143px;">03-5817-2963</div>
    <div class="line contact__detail" style="left:533px; top:168px;">pastor@maplegrovefell.org</div>
    <div class="line contact__detail" style="left:533px; top:191px;">http://www.maplegrovefell.org</div>
    <div class="line contact__detail" style="left:533px; top:237px;">3-9-4 Kawaranodai, Minori-ku,</div>
    <div class="line contact__detail" style="left:533px; top:260px;">Tokyo 190-0412 (Church)</div>
    <div class="line contact__detail" style="left:533px; top:283px;">2-21 Ochibamachi, Minori-ku,</div>
    <div class="line contact__detail" style="left:533px; top:306px;">Tokyo 190-0427 (Home)</div>
  </div>
</section>

<section class="card card--back">
  <div class="brand">
    <div class="line brand-mark" style="left:349px; top:145px;">MBF</div>
    <div class="line brand-name" style="left:349px; top:234px;">MAPLE GROVE FELLOWSHIP</div>
    <div class="brand-rule" style="left:349px; top:252px; width:232px;"></div>
    <div class="line brand-tagline" style="left:349px; top:270px;">Still waters, open door</div>
  </div>
  <div class="line card__url" style="left:349px; top:366px;">www.maplegrovefell.org</div>
</section>

</body>
</html>
```